PPE EQIUPMENT

WE WOULD LIKE TO PRODUCE 2 DIFFERENT BANNERS TO BE PLACED OUTSIDE OF OUR WAREHOUSE TO ADVERTISE THAT WE HAVE FACE MASKS, HAND SANITISERS, DISINFECTANT SPRAY, FACE SHIELDS AND HAND SOAP. THE SIZE OF EACH BANNER WILL BE , portrait to be (W) 140 cm x (H) 250 cm, with 4 x eyelets. THE BANNER IS TO STATE PPE EQUIPMENT AVAILABLE HERE AND SHOW OUR PHONE NUMBER 0207-946-0318. FINALLY WE WILL REQUIRE SOME IMAGES OF THE PRODUCTS IF YOU CAN SUPPLY THESE. THANKS

```html
<!DOCTYPE html>
<html lang="en">
<head>
<meta charset="utf-8">
<title>PPE Equipment Available – Banners</title>
<link rel="stylesheet" href="https://fonts.googleapis.com/css2?family=Open+Sans:wght@600;700;800&family=Roboto+Condensed:wght@400;700&display=swap">
<style>
  :root{
    --page:#e8e9eb;
    --navy:#2f3f6e;
    --navy-deep:#34497a;
    --blue:#1f6fb5;
    --sky:#9ec6e4;
    --grey-text:#4a4f57;
    --dark-top:#3a4e86;
    --dark-mid:#4d7bb8;
    --dark-bottom:#86c8ea;
    --olive:#b6bd4c;
    --yellow:#f2e400;
    --white:#ffffff;
  }
  *{box-sizing:border-box;margin:0;padding:0}
  html,body{width:1200px;height:993px;overflow:hidden}
  body{background:var(--page);position:relative;font-family:"Open Sans",Arial,sans-serif}

  .banner{position:absolute;top:86px;width:459px;height:820px;overflow:hidden}
  .banner--light{left:116px;background:linear-gradient(180deg,#f6f9fc 0%,#dce9f3 35%,#a9bfd8 55%,#4d6496 72%,var(--navy-deep) 85%)}
  .banner--dark{left:625px;background:linear-gradient(180deg,var(--dark-top) 0%,#3f5a94 35%,var(--dark-mid) 65%,#5d9bd0 82%,var(--dark-bottom) 100%)}

  .eyelet{position:absolute;width:18px;height:18px;border-radius:50%;border:2px solid #2a2a2a;background:radial-gradient(circle,#fff 0 3px,#2a2a2a 3px 4px,#fff 4px)}
  .banner--dark .eyelet{border-color:#fff;background:radial-gradient(circle,var(--dark-top) 0 3px,#fff 3px 4px,var(--dark-top) 4px)}
  .eyelet--tl{left:9px;top:8px}.eyelet--tr{right:9px;top:8px}
  .eyelet--bl{left:9px;bottom:8px}.eyelet--br{right:9px;bottom:8px}

  .brand{position:absolute;top:34px;left:33px;right:30px;height:92px;display:flex;align-items:center;gap:18px}
  .brand__mark{width:70px;height:70px;background:var(--navy);flex:none}
  .banner--dark .brand__mark{background:var(--white)}
  .brand__text{flex:1;text-align:center}
  .brand__name{font-family:"Roboto Condensed",Arial,sans-serif;font-weight:400;font-size:25px;color:var(--grey-text);letter-spacing:-.2px;white-space:nowrap}
  .brand__tagline{font-family:"Roboto Condensed",Arial,sans-serif;font-size:13px;color:var(--grey-text);margin-top:2px;letter-spacing:.3px}
  .banner--dark .brand__name,.banner--dark .brand__tagline{color:var(--white)}

  .chevrons{position:absolute;top:161px;width:68px;height:82px}
  .chevrons--left{left:0}
  .chevrons--right{right:0;transform:scaleX(-1)}
  .chevrons path{fill:var(--sky)}
  .banner--dark .chevrons path{fill:var(--olive)}

  .headline{position:absolute;top:150px;left:0;right:0;text-align:center;font-weight:700;font-size:39px;line-height:55px;color:var(--navy);letter-spacing:.5px}
  .banner--dark .headline{color:var(--white)}

  .products-list{position:absolute;top:270px;left:0;right:0;text-align:center;list-style:none;font-weight:700;font-size:24px;line-height:34px;color:var(--blue)}
  .products-list .dot{font-size:18px;margin:0 6px;vertical-align:2px}
  .banner--dark .products-list{color:var(--white)}
  .banner--dark .products-list .dot{color:var(--yellow)}

  .product-photo{position:absolute;top:371px;left:27px;width:406px;height:360px;border-radius:10px}
  .banner--light .product-photo{background:linear-gradient(160deg,rgba(255,255,255,.55),rgba(146,180,222,.55) 60%,rgba(140,170,235,.45))}
  .banner--dark .product-photo{background:linear-gradient(160deg,rgba(255,255,255,.35),rgba(190,215,240,.4) 55%,rgba(230,200,80,.25))}

  .phone{position:absolute;top:740px;left:0;right:0;display:flex;align-items:center;justify-content:center;gap:10px}
  .phone__icon{width:54px;height:54px;flex:none}
  .phone__number{font-family:"Roboto Condensed",Arial,sans-serif;font-weight:700;font-size:56px;letter-spacing:1px;color:var(--white)}
  .banner--dark .phone__number{color:var(--navy);-webkit-text-stroke:1.5px var(--white)}
</style>
</head>
<body>

<section class="banner banner--light">
  <span class="eyelet eyelet--tl"></span><span class="eyelet eyelet--tr"></span>
  <span class="eyelet eyelet--bl"></span><span class="eyelet eyelet--br"></span>
  <header class="brand">
    <span class="brand__mark"></span>
    <div class="brand__text">
      <div class="brand__name">NORTHGATE FURNITURE</div>
      <div class="brand__tagline">TRADE FURNITURE SOLUTIONS</div>
    </div>
  </header>
  <svg class="chevrons chevrons--left" viewBox="0 0 68 82" aria-hidden="true">
    <path d="M0 0h14l26 41-26 41H0l26-41z" opacity=".6"/>
    <path d="M22 0h14l26 41-26 41H22l26-41z"/>
  </svg>
  <svg class="chevrons chevrons--right" viewBox="0 0 68 82" aria-hidden="true">
    <path d="M0 0h14l26 41-26 41H0l26-41z" opacity=".6"/>
    <path d="M22 0h14l26 41-26 41H22l26-41z"/>
  </svg>
  <h1 class="headline">PPE EQUIPMENT<br>AVAILABLE</h1>
  <ul class="products-list">
    <li><span class="dot">•</span>Face Masks <span class="dot">•</span>Hand Sanitisers</li>
    <li><span class="dot">•</span>Disinfectant Spray</li>
    <li><span class="dot">•</span>Face Shields <span class="dot">•</span>Hand Soap</li>
  </ul>
  <div class="product-photo" role="img" aria-label="Product photos: respirator face masks, safety glasses, face shield visor, hand sanitiser bottles, alcohol swab box and blue nitrile glove"></div>
  <div class="phone">
    <svg class="phone__icon" viewBox="0 0 54 54" aria-hidden="true">
      <circle cx="27" cy="27" r="25" fill="#fff"/>
      <circle cx="27" cy="27" r="20" fill="#1f6fb5"/>
      <path d="M20 15c2 0 5 6 5 7s-3 2-3 3c0 3 4 8 7 9 1 0 2-3 3-3s7 3 7 5c0 3-3 5-5 5-9 0-18-10-18-19 0-3 2-7 4-7z" fill="#fff"/>
    </svg>
    <span class="phone__number">0207-946-0318</span>
  </div>
</section>

<section class="banner banner--dark">
  <span class="eyelet eyelet--tl"></span><span class="eyelet eyelet--tr"></span>
  <span class="eyelet eyelet--bl"></span><span class="eyelet eyelet--br"></span>
  <header class="brand">
    <span class="brand__mark"></span>
    <div class="brand__text">
      <div class="brand__name">NORTHGATE FURNITURE</div>
      <div class="brand__tagline">TRADE FURNITURE SOLUTIONS</div>
    </div>
  </header>
  <svg class="chevrons chevrons--left" viewBox="0 0 68 82" aria-hidden="true">
    <path d="M0 0h14l26 41-26 41H0l26-41z" opacity=".45"/>
    <path d="M22 0h14l26 41-26 41H22l26-41z"/>
  </svg>
  <svg class="chevrons chevrons--right" viewBox="0 0 68 82" aria-hidden="true">
    <path d="M0 0h14l26 41-26 41H0l26-41z" opacity=".45"/>
    <path d="M22 0h14l26 41-26 41H22l26-41z"/>
  </svg>
  <h1 class="headline">PPE EQUIPMENT<br>AVAILABLE</h1>
  <ul class="products-list">
    <li><span class="dot">•</span>Face Masks <span class="dot">•</span>Hand Sanitisers</li>
    <li><span class="dot">•</span>Disinfectant Spray</li>
    <li><span class="dot">•</span>Face Shields <span class="dot">•</span>Hand Soap</li>
  </ul>
  <div class="product-photo" role="img" aria-label="Product photos: respirator face masks, safety glasses, yellow face shield visor, hand sanitiser bottles, alcohol swab box and blue nitrile glove"></div>
  <div class="phone">
    <svg class="phone__icon" viewBox="0 0 54 54" aria-hidden="true">
      <circle cx="27" cy="27" r="25" fill="#2f3f6e"/>
      <circle cx="27" cy="27" r="20" fill="#e6ea3a"/>
      <path d="M20 15c2 0 5 6 5 7s-3 2-3 3c0 3 4 8 7 9 1 0 2-3 3-3s7 3 7 5c0 3-3 5-5 5-9 0-18-10-18-19 0-3 2-7 4-7z" fill="#2f3f6e"/>
    </svg>
    <span class="phone__number">0207-946-0318</span>
  </div>
</section>

</body>
</html>
```